Professional Facebook Banner, Business Cards, Door Hang Tags, Service Flyer for Pest Control Company

There are really 4 things I need designed but Pixel Harbor doesn't have them to package together. I am needing to get a Professional Facebook Banner, Business Cards, Door Hang Tags, and Service Flyer for a Pest Control Company. I already have a logo that I will attach to the project along with content a for each one of these tasks. Please see document attached labeled All Design Content & Flyer Content.
Pest Control

```html
<!DOCTYPE html>
<html lang="en">
<head>
<meta charset="utf-8">
<title>Tangerine Ridge Pest Control – Service Flyer</title>
<link href="https://fonts.googleapis.com/css2?family=Open+Sans:wght@400;600;700;800&family=Open+Sans+Condensed:wght@700&display=swap" rel="stylesheet">
<style>
  :root {
    --orange: #e5561a;
    --orange-deep: #d04a12;
    --ink: #111111;
    --panel-black: #0d0d0d;
    --paper: #f4f4f4;
    --header-grey: #ececec;
    --muted: #d8d8d8;
    --backdrop: #e4e4e4;
    --tab: #1a1a1a;
  }
  * { box-sizing: border-box; margin: 0; padding: 0; }
  html, body { width: 1200px; height: 900px; overflow: hidden; }
  body { background: var(--backdrop); font-family: "Open Sans", Arial, sans-serif; position: relative; }

  .flyer { position: absolute; left: 300px; top: 25px; width: 600px; height: 850px; background: var(--paper); overflow: hidden; box-shadow: 0 2px 10px rgba(0,0,0,.12); }

  .header { position: absolute; left: 0; top: 0; width: 600px; height: 84px; background: var(--header-grey); }
  .header-band { position: absolute; left: 0; top: 0; }
  .brand { position: absolute; left: 62px; top: 24px; display: flex; align-items: center; gap: 8px; color: var(--orange); font-weight: 800; font-size: 17px; letter-spacing: .5px; text-transform: uppercase; line-height: 1; }
  .brand-mark { width: 14px; height: 14px; background: var(--orange); }
  .brand-sub { position: absolute; left: 84px; top: 46px; color: var(--orange); font-weight: 800; font-size: 9px; letter-spacing: 6px; }
  .website { position: absolute; left: 318px; top: 30px; width: 282px; text-align: center; color: #fff; font-size: 16px; }
  .header-rule { position: absolute; left: 0; top: 84px; width: 600px; height: 5px; background: var(--ink); }

  .hero { position: absolute; left: 0; top: 89px; width: 600px; height: 274px; background: #f7f7f7; }
  .hero-photo { position: absolute; left: 270px; top: 0; width: 330px; height: 274px; background: linear-gradient(90deg, #f7f7f7 0%, #e7e5e1 30%, #d9d4cc 60%, #c9d3d6 100%); }
  .headline { position: absolute; left: 0; top: 32px; width: 270px; text-align: center; line-height: 1; }
  .headline .kicker { color: var(--orange); font-size: 22px; font-weight: 400; }
  .headline .big { display: block; font-size: 56px; font-weight: 700; color: var(--ink); margin-top: 6px; letter-spacing: -1px; }
  .headline .problems { display: block; color: var(--orange); font-size: 30px; font-weight: 700; margin-top: 4px; }
  .headline .cta { display: block; font-size: 21px; color: var(--ink); margin-top: 8px; }
  .headline .cta em { font-style: normal; color: var(--orange); }
  .headline .cta-2 { display: block; font-size: 21px; color: var(--ink); margin-top: 6px; }

  .info { position: absolute; left: 0; top: 363px; width: 600px; height: 392px; background: var(--panel-black); color: #fff; }
  .info p { position: absolute; left: 22px; width: 340px; font-size: 7.6px; line-height: 13px; color: #e8e8e8; }
  .info .intro { top: 18px; }
  .info .plans { top: 85px; }
  .covered-title { position: absolute; left: 22px; top: 132px; width: 340px; text-align: center; color: var(--orange); font-weight: 700; font-size: 13px; }
  .pest-strip { position: absolute; left: 22px; top: 152px; width: 312px; height: 82px; display: flex; gap: 3px; border-radius: 14px; overflow: hidden; }
  .pest-tile { flex: 1; background: radial-gradient(circle, #d9c7b3 0%, #f1f1f1 70%); }
  .pest-list { top: 246px !important; text-align: justify; font-size: 8px !important; line-height: 12.5px !important; }
  .call-label { position: absolute; left: 30px; top: 332px; color: var(--orange); font-size: 12px; font-weight: 600; }
  .phone { position: absolute; left: 30px; top: 344px; color: #fff; font-size: 34px; font-weight: 400; letter-spacing: .5px; }

  .note { position: absolute; left: 22px; top: 778px; width: 340px; font-size: 7.6px; line-height: 13px; color: #333; }

  .plans-panel { position: absolute; left: 374px; top: 279px; width: 216px; height: 556px; background: var(--orange); border-radius: 14px; }
  .plan { position: absolute; left: 10px; width: 196px; background: #fff; border-radius: 4px; padding: 22px 10px 0 10px; }
  .plan.bronze { top: 11px; height: 152px; }
  .plan.silver { top: 172px; height: 173px; }
  .plan.gold { top: 354px; height: 193px; }
  .plan-tab { position: absolute; top: 3px; left: 50%; transform: translateX(-50%); background: var(--tab); color: #fff; font-size: 8px; padding: 2px 10px; white-space: nowrap; letter-spacing: .2px; }
  .plan ul { list-style: none; font-size: 7.6px; line-height: 12.2px; color: var(--ink); }
  .plan .plus { padding-left: 18px; }
  .plan .extra { font-style: italic; font-weight: 600; }
  .price { position: absolute; left: 10px; bottom: 8px; width: 140px; font-size: 7.6px; border-bottom: 1px dotted #555; line-height: 10px; }
</style>
</head>
<body>
<main class="flyer">
  <header class="header">
    <svg class="header-band" width="600" height="84" viewBox="0 0 600 84" aria-hidden="true">
      <polygon points="305,0 600,0 600,84 273,84" fill="var(--orange-deep)"/>
    </svg>
    <div class="brand"><span class="brand-mark"></span>Tangerine Ridge</div>
    <div class="brand-sub">PEST CONTROL</div>
    <div class="website">www.tangerineridgepest.com</div>
  </header>
  <div class="header-rule"></div>

  <section class="hero">
    <div class="hero-photo" role="img" aria-label="Photo of a smiling technician in cap and overalls giving a thumbs up while spraying a bright room"></div>
    <h1 class="headline">
      <span class="kicker">YOU HAVE</span>
      <span class="big">PEST</span>
      <span class="problems">PROBLEMS</span>
      <span class="cta">schedule your <em>FREE</em></span>
      <span class="cta-2">INSPECTION TODAY!</span>
    </h1>
  </section>

  <section class="info">
    <p class="intro">Pests are constantly trying to enter your home, which can easily cause frustration and damage to your home and belongings. That's why we at Tangerine Ridge Pest Control provide seasonally designed, proactive home pest control plans to protect your family and your home.</p>
    <p class="plans">Our home pest control plans offer effective and affordable solutions to all your pest issues in and around your home.</p>
    <h2 class="covered-title">COVERED PESTS:</h2>
    <div class="pest-strip">
      <div class="pest-tile" role="img" aria-label="Photo of an ant"></div>
      <div class="pest-tile" role="img" aria-label="Photo of a bee"></div>
      <div class="pest-tile" role="img" aria-label="Photo of a box elder bug"></div>
      <div class="pest-tile" role="img" aria-label="Photo of a spider"></div>
    </div>
    <p class="pest-list">Ants, Carpenter Ants, Bees, Carpenter Bees, Box Elder Bugs, Centipedes, Clover Mites, Crickets, General Spiders, Ground Beetles, Earwigs, Millipedes, Mice, Oriental Roaches, Pill Bugs, Sow Bugs, Scorpions, and Wasps all within 10 feet of the structure being treated.</p>
    <div class="call-label">CALL NOW FOR A FREE QUOTE</div>
    <div class="phone">(555) 014-2290</div>
  </section>

  <p class="note">Please Note: to have full guarantee for Asian Beetles, Brown Recluse Spider, Cluster Flies, Lady Bugs, and Silverfish the structures attic and/or crawlspace would need to be treated. There are additional fees for these services</p>

  <aside class="plans-panel">
    <div class="plan bronze">
      <span class="plan-tab">HOME DEFENSE BRONZE</span>
      <ul>
        <li>Year-Round Pest Protection</li>
        <li>Bi-Monthly Service (6 visits per year)</li>
        <li>Covers 15+ Pests</li>
        <li>Exterior Treatment</li>
        <li>Interior Treatment (As Needed)</li>
        <li>Rodent Control</li>
        <li>Stinging Insect Removal</li>
        <li>Free Re-Treatments</li>
      </ul>
      <div class="price">$</div>
    </div>
    <div class="plan silver">
      <span class="plan-tab">HOME DEFENSE SILVER</span>
      <ul>
        <li>Year-Round Pest Protection</li>
        <li>Bi-Monthly Service (6 visits per year)</li>
        <li>Covers 15+ Pests</li>
        <li>Exterior Treatment</li>
        <li>Interior Treatment (As Needed)</li>
        <li>Rodent Control</li>
        <li>Stinging Insect Removal</li>
        <li>Free Re-Treatments</li>
        <li class="plus">+</li>
        <li class="extra">Termite Monitoring &amp;</li>
      </ul>
      <div class="price">$</div>
    </div>
    <div class="plan gold">
      <span class="plan-tab">HOME DEFENSE GOLD</span>
      <ul>
        <li>Year-Round Pest Protection</li>
        <li>Bi-Monthly Service (6 visits per year)</li>
        <li>Covers 15+ Pests</li>
        <li>Exterior Treatment</li>
        <li>Interior Treatment (As Needed)</li>
        <li>Rodent Control</li>
        <li>Stinging Insect Removal</li>
        <li>Free Re-Treatments</li>
        <li class="plus">+</li>
        <li class="extra">Termite Monitoring &amp;<br>Mosquito Reduction Treatments</li>
      </ul>
      <div class="price">$</div>
    </div>
  </aside>
</main>
</body>
</html>
```